Front book cover for a training course to help bakers get higher prices and sell more wedding cakes.

We need a front cover for a book that will be teaching bakers how to sell wedding cakes to get higher prices and book more orders. It is a business book. Do not make it look like we want brides to read it. Bakers will be judging the cover to see if it is worth their investment to read it. The title is already in the logo, so do not repeat it.

Target Market(s)

Bakers who sell wedding cakes

Industry/Entity Type

Bakery

Colors

Designer to choose colors to be used in the design.

Requirements
Must have
• Must use the logo. Must have author name: Lou Brand. Must have subtitle: Boost Your Prices. Book More Brides. Build Your Empire.
Nice to have
• You are free to be creative. The concept is not to be pretty. It is a business sales and marketing book

```html
<!DOCTYPE html>
<html lang="en">
<head>
<meta charset="utf-8">
<title>Cake Profit Pro — Book Cover</title>
<link rel="stylesheet" href="https://fonts.googleapis.com/css2?family=Saira:wght@400;700;800&display=swap">
<style>
  :root {
    --backdrop: #eceeef;
    --paper: #ffffff;
    --brand-pink: #ee4d76;
    --icon-pink: #e53f6a;
    --ink-grey: #4a4a4c;
    --text-white: #ffffff;
  }
  * { margin: 0; padding: 0; box-sizing: border-box; }
  html, body {
    width: 1200px;
    height: 799px;
    overflow: hidden;
    background: var(--backdrop);
  }
  .stage {
    position: relative;
    width: 1200px;
    height: 799px;
  }
  .book-cover {
    position: absolute;
    left: 334px;
    top: 19px;
    width: 532px;
    height: 760px;
    background: var(--paper);
    box-shadow: 0 6px 18px rgba(0, 0, 0, 0.18);
  }
  .book-cover svg { display: block; }
  .brand-name {
    font-family: "Saira", sans-serif;
    font-weight: 800;
    fill: var(--ink-grey);
  }
  .subtitle {
    font-family: "Saira", sans-serif;
    fill: var(--text-white);
    font-size: 37px;
  }
  .subtitle .strong { font-weight: 700; }
  .subtitle .light { font-weight: 400; }
  .author-name {
    font-family: "Saira", sans-serif;
    font-weight: 700;
    font-size: 50px;
    fill: var(--ink-grey);
  }
  .band { fill: var(--brand-pink); }
  .wedge { fill: var(--ink-grey); }
  .connector { stroke: var(--text-white); stroke-width: 1.6; fill: none; }
  .icon-badge circle { fill: var(--icon-pink); stroke: var(--text-white); stroke-width: 2; }
  .brand-dot { fill: var(--brand-pink); }
</style>
</head>
<body>
<main class="stage">
  <article class="book-cover">
    <svg width="532" height="760" viewBox="0 0 532 760" xmlns="http://www.w3.org/2000/svg">
      <!-- brand block -->
      <g class="brand">
        <circle class="brand-dot" cx="58" cy="150" r="24"/>
        <text class="brand-name" x="96" y="168" font-size="50">Cake Profit Pro</text>
      </g>

      <!-- diagonal band with grey wedges -->
      <polygon class="wedge" points="0,236 200,258 0,286"/>
      <polygon class="band" points="0,286 532,228 532,631 0,690"/>
      <polygon class="wedge" points="288,660 532,631 532,690"/>

      <!-- subtitle step 1 -->
      <text class="subtitle" text-anchor="end">
        <tspan class="strong" x="380" y="315">BOOST</tspan>
        <tspan x="380" y="354"><tspan class="light">YOUR </tspan><tspan class="strong">PRICES</tspan></tspan>
      </text>
      <g class="icon-badge" role="img" aria-label="Rocket with dollar sign icon">
        <circle cx="430" cy="320" r="43"/>
      </g>

      <polyline class="connector" points="430,366 430,385 97,385 97,400"/>

      <!-- subtitle step 2 -->
      <g class="icon-badge" role="img" aria-label="Bride icon">
        <circle cx="97" cy="446" r="43"/>
      </g>
      <text class="subtitle">
        <tspan class="strong" x="153" y="440">BOOK</tspan>
        <tspan x="153" y="479"><tspan class="strong">MORE </tspan><tspan class="light">BRIDES</tspan></tspan>
      </text>

      <polyline class="connector" points="97,490 97,513 430,513 430,528"/>

      <!-- subtitle step 3 -->
      <text class="subtitle" text-anchor="end">
        <tspan class="strong" x="380" y="566">BUILD</tspan>
        <tspan x="380" y="606"><tspan class="light">YOUR </tspan><tspan class="strong">EMPIRE</tspan></tspan>
      </text>
      <g class="icon-badge" role="img" aria-label="Skyscraper icon">
        <circle cx="430" cy="572" r="43"/>
      </g>

      <!-- author -->
      <text class="author-name" x="266" y="737" text-anchor="middle">LOU BRAND</text>
    </svg>
  </article>
</main>
</body>
</html>
```